Commercial Auto Insurance Application and Commercial Property Insurance Application

Hi I need a fillable application for my business to send to potential clients for Commercial Auto Insurance and Commercial Property Insurance. I have attached an example application I currently use for another line of insurance.
Commercial Auto Insurance Application
On the first page I would need the following:
- Business Name: (fill in area for text)
- Effective Date: (fill in area for text)
- How do you structure your business? (Check box for “Sole Proprietor”, “Partnership”, “Corporation”, “LLC”)
- Contact Name: (fill in area for text) / Phone Number: (fill in area for text) / Contact Email (fill in area for text)
- Mailing address: (fill in area for text)
- Garaging location: (fill in area for text)
- Owner Name: (fill in area for text)
- Description of Operations: (fill in area for text)
- How long has the operation been in business? (fill in area for text)
- How many years of experience does your management have in the truck/transportation industry? (fill in area for text)
Coverages
Liability Combined Single Limit: ($1,000,000 (checkbox) / $500,000 (checkbox / $300,000 (checkbox) / Other: (fill in area for text)
Uninsured Motorist CSL: (fill in area for text) (checkbox for “Rejected”)
Medical Payments: (fill in area for text)
Physical Damage: (fill in area for text) (checkbox for Rejected)
Liability Deducible: ($500 checkbox, $1,000 checkbox, $2,500 checkbox, $5,000 checkbox)
Physical Damage Deductible: ($500 checkbox, $1,000 checkbox, $2,500 checkbox, $5,000 checkbox)
Driving radius: (fill in area for text)
How many years have you had your own continuous commercial auto insurance coverage for the current business name? (fill in area for text)
Do any of your vehicles travel across state lines? Yes (checkbox)/ No (checkbox)
If yes, please list all states in which vehicles operate: (fill in area for text)
What is the maximum radius traveled for your customer's business?
0-25 miles (checkbox)
26-50 miles (checkbox)
51-75 miles (checkbox)
76-100 miles (checkbox)
101-150 miles (checkbox)
151-200 miles (checkbox)
201-300 miles (checkbox)
300+ miles (checkbox)
Would you like physical damage coverage for this vehicle? (should be for each vehicle listed)
On the 2nd page of the application I would need the following:
I would need to have it where people can fill in the vehicle information such as VIN:, Year:, Make:, Model:, Type of Vehicle:, Trailers:, Value:
I would also need to have it where people can fill in the drivers with their driver info including Name:, DOB:, DL #:, DL State:, Class of License:, Married: Yes/No, Number of years driving similar vehicle:
Please make it where you can fill in 20 vehicle's information and 20 driver's info.
For the 2nd Application I would need one for Property Insurance
On the Commercial Property Application I would need the following:
- Building Address: (fill in area for text)
- Building Description: (fill in area for text)
- Building Amount: $(fill in area for text)
- Business Personal Property Amount: $ (fill in area for text) (checkbox for Not Needed)
- Building Sq Ft: (fill in area for text)
- Total Area Sq Ft: (fill in area for text)
- Building Construction Type: Wood Frame (checkbox), Steel (checkbox), Fire Resistive (checkbox), Non-Combustible (checkbox), Other (fill in area for text)
- # of stories: (fill in area for text)
- Year Built: (fill in area for text)
- Wiring improvement year: (fill in area for text)
- Roofing improvement year: (fill in area for text)
- Plumbing improvement year: (fill in area for text)
- Heating improvement year: (fill in area for text)
- What is to the right of the building and distance: (fill in area for text)
- What is to the left of the building and distance: (fill in area for text)
- What is in front of the building and distance: (fill in area for text)
- What is behind the building and distance: (fill in area for text)
- Burglar alarm installation and serviced by: (fill in area for text) None (checkbox)
- Does the premises have fire protection? Sprinkler system (checkbox), Fire detection (checkbox), Other: (fill in area for text) None (checkbox)

```html
<!DOCTYPE html>
<html lang="en">
<head>
<meta charset="utf-8">
<title>Application Commercial Auto Insurance</title>
<link href="https://fonts.googleapis.com/css2?family=Montserrat:wght@700;800&family=Source+Sans+3:wght@400;600;700&display=swap" rel="stylesheet">
<style>
  :root{
    --navy:#2b3f86;
    --title-blue:#3e58a6;
    --label:#2e3d6b;
    --line:#4a5ea8;
    --green:#17a04b;
    --box-ink:#1e1e1e;
    --paper:#ffffff;
  }
  *{box-sizing:border-box;margin:0;padding:0}
  html,body{width:856px;height:1200px;overflow:hidden;background:var(--paper)}
  body{font-family:"Source Sans 3",Arial,sans-serif;color:var(--label);position:relative}

  .brand{position:absolute;left:39px;top:66px;display:flex;align-items:center;gap:10px}
  .brand-mark{width:18px;height:18px;background:var(--green)}
  .brand-name{font-family:"Source Sans 3",Arial,sans-serif;font-weight:700;font-size:40px;letter-spacing:1px;color:var(--navy);line-height:1}

  .agency{position:absolute;right:54px;top:38px;text-align:right;font-size:15.5px;line-height:21.8px;color:#2a2a2a}

  .title{position:absolute;left:0;width:856px;top:146px;text-align:center;font-family:"Montserrat",Arial,sans-serif;font-weight:800;font-size:33px;color:var(--title-blue);letter-spacing:.2px}

  .form{position:absolute;top:193.4px;left:0;width:856px;display:grid;grid-template-rows:repeat(27,34.8px)}
  .row{position:relative}
  .label,.opt{position:absolute;left:var(--x);top:0;height:34.8px;display:flex;align-items:center;font-size:14.6px;white-space:nowrap;color:var(--label)}
  .field{position:absolute;left:var(--x);right:var(--r,51px);top:0;height:34.8px;border:1px solid var(--line);display:flex;align-items:center;padding-left:6px;font-size:14.6px;color:var(--label);background:var(--paper)}
  .field.stub{border-right:1px solid var(--line)}
  .opt{gap:3px}
  .check{width:24px;height:24px;border:2px solid #1b1b1b;background:var(--paper);flex:none}

  .band{position:absolute;left:35px;right:51px;top:0;height:34.8px;background:var(--green);color:#fff;display:flex;align-items:center;padding-left:3px}
  .band.section{font-weight:700;font-size:18px}
  .band.question{font-size:14.6px}
</style>
</head>
<body>
  <div class="brand">
    <span class="brand-name">RIDGELINE</span>
    <span class="brand-mark"></span>
  </div>

  <address class="agency" style="font-style:normal">
    Ridgeline Insurance Services<br>
    2480 Alder Park Way Suite 310<br>
    Cedar Falls, CA 91520<br>
    Tel: (555) 014-2280
  </address>

  <h1 class="title">Application Commercial Auto Insurance</h1>

  <main class="form">
    <div class="row"><span class="label" style="--x:38px">Business Name:</span><div class="field" style="--x:161px">(fill in area for text)</div></div>
    <div class="row"><span class="label" style="--x:38px">- Effective Date:</span><div class="field" style="--x:161px">(fill in area for text)</div></div>
    <div class="row">
      <span class="label" style="--x:38px">- How do you structure your business?</span>
      <span class="opt" style="--x:292px"><span class="check"></span>Sole Proprietor</span>
      <span class="opt" style="--x:446px"><span class="check"></span>Partnership</span>
      <span class="opt" style="--x:603px"><span class="check"></span>Corporation</span>
      <span class="opt" style="--x:751px"><span class="check"></span>LLC</span>
    </div>
    <div class="row"><span class="label" style="--x:38px">- Contact Name</span><div class="field" style="--x:161px"></div></div>
    <div class="row">
      <span class="label" style="--x:38px">Phone Number</span>
      <div class="field" style="--x:161px;--r:527px"></div>
      <div class="field" style="--x:329px;--r:485px">Email</div>
      <div class="field" style="--x:371px;--r:52px">(fill in area for text for each)</div>
    </div>
    <div class="row"><span class="label" style="--x:41px">Mailing address:</span><div class="field" style="--x:161px">(fill in area for text)</div></div>
    <div class="row"><span class="label" style="--x:41px">Garaging location:</span><div class="field" style="--x:161px">(fill in area for text)</div></div>
    <div class="row"><span class="label" style="--x:41px">Owner Name:</span><div class="field" style="--x:161px">(fill in area for text)</div></div>
    <div class="row"><span class="label" style="--x:41px">Description of Operations:</span><div class="field" style="--x:213px">(fill in area for text)</div></div>
    <div class="row"><span class="label" style="--x:41px">How long has operation been in business?</span><div class="field" style="--x:313px">(fill in area for text)</div></div>
    <div class="row"><span class="label" style="--x:41px">How many years of experience does your management have in the truck/transportation business?</span><div class="field" style="--x:656px;--r:51px;padding-left:2px">(fill in area for text)</div></div>

    <div class="row"><div class="band section">Coverages</div></div>
    <div class="row">
      <span class="label" style="--x:38px">Liability Combined Single Limit:</span>
      <span class="opt" style="--x:241px"><span class="check"></span>$1,000,000</span>
      <span class="opt" style="--x:354px"><span class="check"></span>$500,000</span>
      <span class="opt" style="--x:470px"><span class="check"></span>$300,000</span>
      <span class="opt" style="--x:563px"><span class="check"></span>Other:</span>
      <div class="field" style="--x:629px;padding-left:2px">(fill in area for text)</div>
    </div>
    <div class="row">
      <span class="label" style="--x:38px">Uninsured Motorist CSL:</span>
      <div class="field" style="--x:192px;--r:241px">(fill in area for text)</div>
      <span class="label" style="--x:630px">Rejected</span>
    </div>
    <div class="row"><span class="label" style="--x:38px">Medical Payments:</span><div class="field" style="--x:158px">(fill in area for text)</div></div>
    <div class="row"><span class="label" style="--x:38px">Physical Damage:</span><div class="field" style="--x:158px">(fill in area for text)</div></div>
    <div class="row">
      <span class="label" style="--x:38px">Liability Deducible:</span>
      <span class="opt" style="--x:242px"><span class="check"></span>($500,</span>
      <span class="opt" style="--x:361px"><span class="check"></span>$1,000,</span>
      <span class="opt" style="--x:528px"><span class="check"></span>$2,500,</span>
      <span class="opt" style="--x:689px"><span class="check"></span>$5,000)</span>
    </div>
    <div class="row">
      <span class="label" style="--x:38px">Physical Damage Deductible:</span>
      <span class="opt" style="--x:242px"><span class="check"></span>($500,</span>
      <span class="opt" style="--x:361px"><span class="check"></span>$1,000,</span>
      <span class="opt" style="--x:528px"><span class="check"></span>$2,500,</span>
      <span class="opt" style="--x:689px"><span class="check"></span>$5,000)</span>
    </div>
    <div class="row"><span class="label" style="--x:38px">Driving radius:</span><div class="field" style="--x:158px">(fill in area for text)</div></div>
    <div class="row"><span class="label" style="--x:38px">How many years have you had your own continuous commercial auto insurance coverage for the current business name?</span></div>
    <div class="row"><div class="field" style="--x:35px;padding-left:2px">(fill in area for text)</div></div>
    <div class="row">
      <span class="label" style="--x:38px">Do any of your vehicles travel across state lines?</span>
      <span class="opt" style="--x:392px"><span class="check"></span>Yes/</span>
      <span class="opt" style="--x:584px"><span class="check"></span>No</span>
    </div>
    <div class="row"><span class="label" style="--x:38px">If yes, please list all states in which vehicles operate:</span><div class="field" style="--x:364px">(fill in area for text)</div></div>

    <div class="row"><div class="band question">What is the maximum radius traveled for your customer's business?</div></div>
    <div class="row">
      <span class="opt" style="--x:111px"><span class="check"></span>0-25 miles</span>
      <span class="opt" style="--x:320px"><span class="check"></span>26-50 miles</span>
      <span class="opt" style="--x:466px"><span class="check"></span>51-75 miles</span>
      <span class="opt" style="--x:666px"><span class="check"></span>76-100 miles</span>
    </div>
    <div class="row">
      <span class="opt" style="--x:111px"><span class="check"></span>101-150 miles</span>
      <span class="opt" style="--x:320px"><span class="check"></span>151-200 miles</span>
      <span class="opt" style="--x:466px"><span class="check"></span>201-300 miles</span>
      <span class="opt" style="--x:666px"><span class="check"></span>300+ miles</span>
    </div>
    <div class="row"><span class="label" style="--x:38px">Would you like physical damage coverage for this vehicle?</span><div class="field" style="--x:403px;padding-left:4px">(should be for each vehicle listed)</div></div>
  </main>
</body>
</html>
```